Small butcher shop from Austria needs great powerpoint presentation

We are looking for a powerpoint template for our new CI - it should be modern and clear.

Logo (2 Versions), Slogan, Business Card and Car-Wrap-Design already exist. (See documents below.)

We won't use much text. About 50% of the presentation should be pictures, included in different ways.

We are a family business in Upper Austria, only process animals from farms in the immediate vicinity, produce the products by hand, value animal welfare and short transport routes and avoid packaging as much as possible.

The design should be modern and clear.

Font styles to use
Sans Serif

Requirements
Should not have
• Use the red color sparingly. Only use sans serif fonts (Myriad Pro - if possible). The logo needs to be on first and last page only.

```html
<!DOCTYPE html>
<html lang="en">
<head>
<meta charset="utf-8">
<title>Kranzl Fleischhauerei – Presentation Template</title>
<link rel="stylesheet" href="https://fonts.googleapis.com/css2?family=Poppins:ital,wght@0,400;0,500;0,600;0,700;1,500&display=swap">
<style>
:root{
  --page:#eef0f2;
  --wine:#7e1020;
  --wine-deep:#6c0c1a;
  --wine-soft:#8e1c2b;
  --char:#2b2426;
  --char-deep:#1f1a1b;
  --char-soft:#3a3133;
  --white:#ffffff;
  --ink:#1d1d1f;
  --body:#333336;
  --rule:#d9d9dc;
}
*{box-sizing:border-box;margin:0;padding:0}
html,body{width:1200px;height:3987px;overflow:hidden}
body{background:var(--page);font-family:"Poppins",sans-serif;color:var(--ink);position:relative}
.slide{position:absolute;left:67px;width:1066px;height:600px;overflow:hidden;background:var(--white);box-shadow:0 2px 10px rgba(0,0,0,.08)}
.s1{top:77px}.s2{top:752px}.s3{top:1406px}.s4{top:2054px}.s5{top:2703px}.s6{top:3347px}

.brand{font-family:"Poppins",sans-serif;font-weight:600;letter-spacing:4px;line-height:1;white-space:nowrap;color:var(--white)}

/* cover */
.cover-bg{position:absolute;inset:0;background:linear-gradient(135deg,var(--wine-soft) 0%,var(--wine) 55%,var(--wine-deep) 100%)}
.cover-brand{position:absolute;left:223px;top:279px;transform:translate(-50%,-50%);font-size:64px}
.cover-rule{position:absolute;left:422px;right:0;height:1px;background:rgba(255,255,255,.35)}
.cover-title{position:absolute;left:430px;top:228px;color:var(--white);font-weight:700;font-size:64px;line-height:1;white-space:nowrap}
.cover-sub{position:absolute;left:432px;top:310px;color:var(--white);font-weight:500;font-size:36px;line-height:1;white-space:nowrap}
.cover-web{position:absolute;left:0;right:0;top:552px;text-align:center;color:var(--white);font-size:17px;font-weight:500;letter-spacing:6px}

/* content slides */
.side-band{position:absolute;left:0;top:0;bottom:0;background:linear-gradient(160deg,var(--char-soft),var(--char-deep))}
.photo{position:absolute}
.headline{position:absolute;left:577px;top:114px;width:475px;font-weight:600;font-size:25px;line-height:1.38;color:var(--ink)}
.copy{position:absolute;left:577px;top:202px;width:470px;font-size:14.6px;line-height:30.5px;color:var(--body)}
.page-no{position:absolute;left:1008px;top:542px;width:90px;height:90px;border-radius:50%;background:var(--wine);color:var(--white);font-weight:700;font-size:22px;padding:22px 0 0 22px}

.feature{position:absolute;left:603px;width:450px;height:80px}
.feature-num{position:absolute;left:0;top:0;width:79px;height:79px;border-radius:50%;background:var(--wine);color:var(--white);font-weight:600;font-size:26px;display:flex;align-items:center;justify-content:center}
.feature-title{position:absolute;left:92px;top:6px;font-weight:600;font-size:22px;line-height:1.2}
.feature-text{position:absolute;left:92px;top:37px;width:360px;font-size:14px;line-height:23px;color:var(--body)}
.feature-rule{position:absolute;left:695px;width:348px;height:1px;background:var(--rule)}

/* quote */
.quote-bg{position:absolute;inset:0;background:linear-gradient(160deg,var(--char-deep),var(--char) 50%,var(--char-soft))}
.quote-frame{position:absolute;left:16px;top:16px;right:16px;bottom:16px;border:3px solid var(--white)}
.quote-line{position:absolute;height:2px;background:rgba(255,255,255,.85)}
.quote-dot{position:absolute;width:8px;height:8px;border-radius:50%;background:var(--white)}
.quote-mark{position:absolute;left:502px;top:177px;width:56px;height:56px;border-radius:50%;background:var(--white)}
.quote-text{position:absolute;left:103px;width:860px;top:248px;text-align:center;color:var(--white);font-style:italic;font-weight:500;font-size:17.5px;line-height:34px;white-space:nowrap}
.quote-author{position:absolute;left:0;right:0;top:361px;text-align:center;color:var(--white);font-weight:500;font-size:17px}

/* closing */
.thanks-bg{position:absolute;left:0;top:0;width:100%;height:405px;background:linear-gradient(135deg,var(--wine-soft),var(--wine) 50%,var(--wine-deep))}
.thanks-brand{position:absolute;left:50%;top:137px;transform:translate(-50%,-50%);font-size:62px}
.thanks-title{position:absolute;left:0;right:0;top:252px;text-align:center;color:var(--white);font-weight:600;font-size:42px;line-height:1}
.thanks-divider{position:absolute;left:0;right:0;top:403px;height:4px;background:#b9c3bf}
.contact{position:absolute;top:374px;width:260px;text-align:center}
.contact-icon{width:58px;height:58px;margin:0 auto;background:var(--white);box-shadow:0 2px 6px rgba(0,0,0,.15);display:flex;align-items:center;justify-content:center}
.contact-text{margin-top:14px;font-size:15px;line-height:22px;color:var(--body)}
</style>
</head>
<body>

<!-- Cover -->
<section class="slide s1">
  <div class="cover-bg" role="img" aria-label="Faded red-toned photograph of an old town skyline with rooftops and a church dome"></div>
  <div class="brand cover-brand">KRANZL</div>
  <div class="cover-rule" style="top:209px"></div>
  <h1 class="cover-title">Presentation Title</h1>
  <p class="cover-sub">Subtitle Of The Presentation</p>
  <div class="cover-rule" style="top:392px"></div>
  <p class="cover-web">WWW.KRANZLFLEISCHHAUEREI.COM</p>
</section>

<!-- Text and image -->
<section class="slide s2">
  <div class="side-band" style="width:279px" role="img" aria-label="Dark toned photograph of meat cuts"></div>
  <div class="photo" style="left:90px;top:51px;width:443px;height:499px;background:linear-gradient(180deg,#9fb9d6 0%,#8a6e5e 35%,#4f5556 60%,#5f7a3e 85%,#6f8f3a 100%)" role="img" aria-label="Delivery van with butcher cut lettering parked in front of a brick farm building"></div>
  <h2 class="headline">The standard Lorem Ipsum passage, used since the 1500s</h2>
  <p class="copy">Sed ut perspiciatis unde omnis iste natus eptatem accusantium doloremque laudantium, totam rem aperiam, eaque ipsa quae ab illo inventore veritatis et quasi architecto beatae vitae dicta sunt explicabo. Nemo enim ipsam voluptatem quia voluptas sit aspernatur aut odit aut fugit, sed qunsequuntur magni dolores eos qui ratione voluptatem sequesciunt. Neque porro quisquam est, qui dolorem ipsum quia dolor sit amet, consectetur, adipisci velit, sed quia non numquam eius di tempora incidunt ut labore et dolore magnam aliquam quaerat voluptatem.</p>
  <div class="page-no">01</div>
</section>

<!-- Image gallery and features -->
<section class="slide s3">
  <div class="side-band" style="width:443px"></div>
  <div class="photo" style="left:20px;top:50px;width:205px;height:333px;background:linear-gradient(150deg,#3a2a22,#7b2a2a 50%,#2c211c)" role="img" aria-label="Hands holding a raw beef cut on a wooden board"></div>
  <div class="photo" style="left:20px;top:398px;width:205px;height:152px;background:linear-gradient(120deg,#5a4a58,#a05a66 50%,#c9c2c4)" role="img" aria-label="Butcher carrying a carcass in a cold room"></div>
  <div class="photo" style="left:241px;top:50px;width:332px;height:500px;background:linear-gradient(180deg,#9cc6cc 0%,#93bfc5 45%,#2b2b2e 75%,#1e1e20 100%)" role="img" aria-label="Smiling bearded butcher in an apron holding a steak and a cleaver"></div>

  <div class="feature" style="top:141px">
    <div class="feature-num">01</div>
    <h3 class="feature-title">The standard Lorem</h3>
    <p class="feature-text">Sed ut perspiciatcusantiuremque laudantium, totam rem aperiam, eaque ie ab illo</p>
  </div>
  <div class="feature-rule" style="top:245px"></div>
  <div class="feature" style="top:269px">
    <div class="feature-num">02</div>
    <h3 class="feature-title">The standard Lorem</h3>
    <p class="feature-text">Sed ut perspiciatcusantiuremque laudantium, totam rem aperiam, eaque ie ab illo</p>
  </div>
  <div class="feature-rule" style="top:372px"></div>
  <div class="feature" style="top:396px">
    <div class="feature-num">03</div>
    <h3 class="feature-title">The standard Lorem</h3>
    <p class="feature-text">Sed ut perspiciatcusantiuremque laudantium, totam rem aperiam, eaque ie ab illo</p>
  </div>
  <div class="page-no">02</div>
</section>

<!-- Quote -->
<section class="slide s4">
  <div class="quote-bg"></div>
  <div class="quote-frame"></div>
  <div class="quote-line" style="left:140px;width:784px;top:204px"></div>
  <div class="quote-dot" style="left:136px;top:201px"></div>
  <div class="quote-dot" style="left:920px;top:201px"></div>
  <div class="quote-mark">
    <svg width="56" height="56" viewBox="0 0 56 56" aria-hidden="true">
      <path d="M17 37c-3 0-5-2.5-5-6 0-6 4-11 10-13l1.5 2.5c-3 1.4-5 3.8-5.3 6.5 3 0 5 2.2 5 5s-2.4 5-6.2 5z" fill="#7e1020"/>
      <path d="M33 37c-3 0-5-2.5-5-6 0-6 4-11 10-13l1.5 2.5c-3 1.4-5 3.8-5.3 6.5 3 0 5 2.2 5 5s-2.4 5-6.2 5z" fill="#7e1020"/>
    </svg>
  </div>
  <p class="quote-text">Lorem ipsum dolor sit amet, consectetur adipiscing elit, sed do eiusmod tempor incididunt ut<br>labore et dolore magna aliqua. Quis ipsum suspendisse ultrices gravida. Risus commodo viverra<br>maecenas accumsan lacus vel facilisis.</p>
  <p class="quote-author">- Anna Berger</p>
  <div class="quote-line" style="left:251px;width:561px;top:410px"></div>
  <div class="quote-dot" style="left:247px;top:407px"></div>
  <div class="quote-dot" style="left:808px;top:407px"></div>
</section>

<!-- Text and image 2 -->
<section class="slide s5">
  <div class="side-band" style="width:279px" role="img" aria-label="Dark toned photograph of meat cuts"></div>
  <div class="photo" style="left:90px;top:51px;width:443px;height:499px;background:linear-gradient(180deg,#6a4c40 0%,#3f4b63 30%,#4b5568 60%,#5d8a3a 82%,#78a341 100%)" role="img" aria-label="Close view of the delivery van side with cut names lettered on it"></div>
  <h2 class="headline">The standard Lorem Ipsum passage, used since the 1500s</h2>
  <p class="copy">Sed ut perspiciatis unde omnis iste natus eptatem accusantium doloremque laudantium, totam rem aperiam, eaque ipsa quae ab illo inventore veritatis et quasi architecto beatae vitae dicta sunt explicabo. Nemo enim ipsam voluptatem quia voluptas sit aspernatur aut odit aut fugit, sed qunsequuntur magni dolores eos qui ratione voluptatem sequesciunt. Neque porro quisquam est, qui dolorem ipsum quia dolor sit amet, consectetur, adipisci velit, sed quia non numquam eius di tempora incidunt ut labore et dolore magnam aliquam quaerat voluptatem.</p>
  <div class="page-no">05</div>
</section>

<!-- Closing -->
<section class="slide s6">
  <div class="thanks-bg" role="img" aria-label="Red-toned photograph of raw meat cuts"></div>
  <div class="brand thanks-brand">KRANZL</div>
  <h2 class="thanks-title">THANK YOU</h2>
  <div class="thanks-divider"></div>

  <div class="contact" style="left:71px">
    <div class="contact-icon">
      <svg width="22" height="26" viewBox="0 0 22 26" aria-hidden="true"><path d="M11 1C5.5 1 1.5 5 1.5 10.2 1.5 17 11 25 11 25s9.5-8 9.5-14.8C20.5 5 16.5 1 11 1z" fill="#7e1020"/><circle cx="11" cy="10" r="3.6" fill="#fff"/></svg>
    </div>
    <p class="contact-text">1234 Somestreet Anywhere<br>USA 21212</p>
  </div>
  <div class="contact" style="left:393px">
    <div class="contact-icon">
      <svg width="26" height="26" viewBox="0 0 26 26" aria-hidden="true"><path d="M6 2l4 5-2.5 3c1.5 3.2 4.3 6 7.5 7.5l3-2.5 5 4-2 4.5C12 23 3 14 1.5 4z" fill="#7e1020"/><path d="M16 3a8 8 0 0 1 7 7M16 7a4 4 0 0 1 3 3" stroke="#7e1020" stroke-width="1.6" fill="none"/></svg>
    </div>
    <p class="contact-text">Phone:<br>(888) 888 - 8888</p>
  </div>
  <div class="contact" style="left:710px">
    <div class="contact-icon">
      <svg width="28" height="20" viewBox="0 0 28 20" aria-hidden="true"><rect x="1" y="1" width="26" height="18" fill="#7e1020"/><path d="M1 1l13 10L27 1M1 19l9-8M27 19l-9-8" stroke="#fff" stroke-width="1.6" fill="none"/></svg>
    </div>
    <p class="contact-text">Email:<br>info@kranzlfleischhauerei.com</p>
  </div>
</section>

</body>
</html>
```